Redesign of Smart Watch Gift Voucher-SEE ATTACHED CURRENT DESIGN

I need to redesign my existing design using all same content and elements.

MY ENVISION: I invision more of a professional advertisement type of flyer/voucher. Imagine how Corvel.com would create a professionally looking flyer promoting the lumo or veno.

you can get many ideas about professional design by looking at some of corvels flyer designs :
https://www.findora-example.net/search?q=lumo+advertisment&mode=img&ref=a83kd02mzq7

stock photos are attached, you do not have to use them all, you can use some or none i am open to your designs using your own images if you want...just make sure the smartwatch looks black

DO NOT LEAVE ANY CONTENT OR ELEMENTS OUT ON MOCK UP PLEASE

SEE ATTACHED CURRENT DESIGN

I need to redesign my existing design using all same content and elements. DO NOT LEAVE ANY CONTENT OR ELEMENTS OUT ON MOCK UP PLEASE

Target Market(s)

B2B-you can get many ideas about professional design by looking at some of corvels flyer designs :

Industry/Entity Type

Marketing

Requirements
Must have
• I need to redesign my existing design using all same content and elements. DO NOT LEAVE ANY CONTENT OR ELEMENTS OUT ON MOCK UP PLEASE

Nice to have

Should not have

```html
<!DOCTYPE html>
<html lang="en">
<head>
<meta charset="UTF-8">
<title>Smart Fitness Watch Reward Voucher</title>
<link rel="stylesheet" href="https://fonts.googleapis.com/css2?family=Baloo+2:wght@400;700;800&family=Raleway:ital,wght@0,400;0,500;1,700&display=swap">
<style>
  :root {
    --navy: #1b2a4d;
    --red: #b20c0c;
    --orange: #ff8500;
    --ink: #1f2a44;
    --rule: #9a9a9a;
    --halo: #f1f1f1;
    --white: #ffffff;
  }
  * { margin: 0; padding: 0; box-sizing: border-box; }
  html, body { width: 849px; height: 1200px; overflow: hidden; background: var(--white); }
  .voucher { position: relative; width: 849px; height: 1200px; overflow: hidden; font-family: "Raleway", sans-serif; color: var(--ink); }

  .hero { position: absolute; left: 0; top: 0; width: 849px; height: 380px; }
  .hero svg { position: absolute; left: 0; top: 0; }
  .hero-title { position: absolute; left: 472px; top: 30px; font-family: "Baloo 2", sans-serif; font-weight: 800; color: var(--white); font-size: 48px; line-height: 57px; letter-spacing: 1px; }
  .hero-title .accent { color: var(--orange); font-size: 51px; display: block; }
  .hero-bar { position: absolute; left: 474px; top: 212px; width: 96px; height: 4px; background: var(--orange); border-radius: 2px; }
  .hero-sub { position: absolute; left: 472px; top: 226px; font-family: "Baloo 2", sans-serif; font-weight: 400; color: var(--white); font-size: 30px; line-height: 41.5px; }

  .intro { position: absolute; left: 28px; top: 400px; width: 795px; font-size: 16.4px; line-height: 27.2px; }
  .intro .lead { color: var(--red); }

  .rule { position: absolute; left: 28px; width: 793px; height: 1px; background: var(--rule); }

  .features-title { position: absolute; left: 0; width: 849px; top: 553px; text-align: center; font-family: "Baloo 2", sans-serif; font-weight: 800; color: var(--red); font-size: 31px; letter-spacing: 1px; }
  .features-bar { position: absolute; left: 395px; top: 599px; width: 68px; height: 5px; background: var(--red); border-radius: 3px; }

  .feature-list { position: absolute; list-style: none; font-size: 18px; }
  .feature-list li { height: 34.2px; display: flex; align-items: center; gap: 14px; }
  .feature-list.left { right: 527px; top: 627px; }
  .feature-list.left li { justify-content: flex-end; }
  .feature-list.right { left: 541px; top: 627px; }
  .feature-list.right li { gap: 21px; }
  .mark { width: 10px; height: 10px; flex: none; }
  .mark.red { background: var(--red); }
  .mark.orange { background: var(--orange); }

  .product { position: absolute; left: 327px; top: 647px; width: 206px; height: 206px; border-radius: 50%; background: var(--halo); }
  .product-shot { position: absolute; left: 30px; top: 10px; width: 146px; height: 186px; border-radius: 40px; background: linear-gradient(160deg, #3a3a3a, #111 70%); }

  .section-head { position: absolute; left: 28px; font-family: "Baloo 2", sans-serif; font-weight: 800; color: var(--red); font-size: 15.5px; letter-spacing: .3px; }
  .story { position: absolute; left: 28px; top: 920px; width: 800px; font-size: 13.6px; line-height: 28.5px; }
  .quote { position: absolute; left: 28px; top: 1075px; font-size: 13.6px; font-style: italic; font-weight: 700; }

  .footer { position: absolute; left: 0; top: 1123px; width: 849px; height: 77px; }
  .footer svg { position: absolute; left: 0; top: 0; }
  .cert { position: absolute; left: 27px; top: 14px; font-family: "Baloo 2", sans-serif; font-weight: 800; color: var(--white); font-size: 15.5px; line-height: 21px; }
  .cert span { color: var(--orange); }
  .redeem { position: absolute; left: 350px; top: 6px; font-family: "Baloo 2", sans-serif; font-weight: 800; color: var(--white); font-size: 15.5px; line-height: 20px; }
  .redeem .url { color: var(--orange); display: block; }
  .terms { position: absolute; left: 351px; top: 52px; font-size: 10.5px; font-style: italic; color: var(--white); }
</style>
</head>
<body>
<div class="voucher">

  <header class="hero">
    <svg width="849" height="380" viewBox="0 0 849 380">
      <defs>
        <linearGradient id="wristTone" x1="0" y1="0" x2="1" y2="1">
          <stop offset="0" stop-color="#8f8f96"/>
          <stop offset=".45" stop-color="#d9a590"/>
          <stop offset="1" stop-color="#2b3140"/>
        </linearGradient>
      </defs>
      <rect width="520" height="380" fill="url(#wristTone)" role="img" aria-label="Photo of a hand touching a black smartwatch on a wrist"/>
      <path d="M470 0 C398 60 378 250 482 380 L470 380 C370 255 390 60 462 0 Z" fill="var(--orange)"/>
      <path d="M474 0 C402 60 382 250 486 380 L849 380 L849 0 Z" fill="var(--navy)"/>
      <path d="M784 0 L849 0 L849 82 Z" fill="var(--red)"/>
      <path d="M0 312 L86 380 L0 380 Z" fill="var(--red)"/>
      <path d="M832 380 L849 363 L849 380 Z" fill="var(--white)"/>
    </svg>
    <h1 class="hero-title">ENJOY YOUR<br>BRAND NEW<span class="accent">SMARTWATCH</span></h1>
    <div class="hero-bar"></div>
    <p class="hero-sub">Take control of your<br>life with your new<br>smart fitness watch</p>
  </header>

  <p class="intro"><span class="lead">Congratulations,</span> you have been rewarded with a Brand New Smart Fitness Watch shipped right to your door. Just pay shipping and handling. Your new Smart Fitness Watch has these features: sport mode, pedometer, distance, calorie, heart rate, blood pressure, stopwatch, sleep monitoring, phone locator, reminders, remote camera, an alarm clock and much more!</p>

  <div class="rule" style="top:531px"></div>

  <h2 class="features-title">FEATURES</h2>
  <div class="features-bar"></div>

  <ul class="feature-list left">
    <li>Pedomoter <span class="mark red"></span></li>
    <li>Calorie Counter <span class="mark orange"></span></li>
    <li>Blood Pressure Monitor <span class="mark red"></span></li>
    <li>Sleep Monitoring <span class="mark orange"></span></li>
    <li>Reminders Feature <span class="mark red"></span></li>
    <li>Alarm Clock <span class="mark orange"></span></li>
  </ul>

  <div class="product">
    <div class="product-shot" role="img" aria-label="Black round smartwatch showing app icons and the time"></div>
  </div>

  <ul class="feature-list right">
    <li><span class="mark red"></span>Distance Tracker</li>
    <li><span class="mark orange"></span>Heart Rate Monitor</li>
    <li><span class="mark red"></span>Stopwatch</li>
    <li><span class="mark orange"></span>Phone Locator</li>
    <li><span class="mark red"></span>Remote Camera</li>
    <li><span class="mark orange"></span>Waterproof</li>
  </ul>

  <div class="rule" style="top:871px"></div>

  <h3 class="section-head" style="top:895px">HOW CAN WE DO THIS?</h3>
  <p class="story">We have a couple retail partners that we team up with to "crowd purchase" huge shipping containers that hold 10's of thousands of electronic products at 80-90% off retail. We simply pass our savings on to you as we do not profit from our electronic products. You are basically able to "piggy back" on our partnerships and buying power to get an attractive electronic premium for a fraction of the retail cost.</p>

  <h3 class="section-head" style="top:1045px">WHAT OTHERS SAY</h3>
  <p class="quote">"Are you sure this is not a Norvik Pulse Smartwatch in DISGUISE???? I love mine." Dale M. Atlantic City, NJ</p>

  <footer class="footer">
    <svg width="849" height="77" viewBox="0 0 849 77">
      <rect width="849" height="77" fill="var(--red)"/>
      <path d="M0 0 L288 0 L329 77 L0 77 Z" fill="var(--navy)"/>
    </svg>
    <p class="cert">CERTIFICATE ID <span>91772-89218</span><br>EXPIRES <span>10/03/2020</span></p>
    <p class="redeem">View all the details of this special offer and redeem online at<span class="url">www.perkvaultrewards.com</span></p>
    <p class="terms">*terms and conditions apply see website for details</p>
  </footer>

</div>
</body>
</html>
```